Commercial and Residential Paint Contractor needs website

We need a website for our residential painting, multi-family painting and commercial painting company. We paint interior and exterior of houses, apartments and commercial buildings. I would like an about us page, residential page, multi family page, commercial page and contact us. Need keywords added to website for seo opitimazation. I like this website https://www.velmorandhalestudio.com/

Target Market(s)

General Contractors and commercial property managers

Coding

Coded - Design and coding required

Number of Pages Required

5+ page

Font styles to use
Sans Serif

Requirements
Must have
• I need SEO keywords on pages

```html
<!DOCTYPE html>
<html lang="en">
<head>
<meta charset="utf-8">
<title>Halden Painting – Commercial and Residential Paint Contractor</title>
<meta name="description" content="Halden Painting – commercial, residential and multi family painting contractor in Chicago. Interior and exterior painting for houses, apartments and commercial buildings.">
<link rel="stylesheet" href="https://fonts.googleapis.com/css2?family=Fira+Sans:wght@300;400;500;600&family=Fira+Sans+Condensed:wght@400&display=swap">
<style>
:root{
  --blue:#1b4c9c;
  --blue-deep:#23317e;
  --red:#d0202a;
  --text:#8a8a8a;
  --dark:#3d3d3d;
  --band:#f4f4f4;
  --testimonial:#58524f;
  --white:#ffffff;
  --rule:#e2e2e2;
}
*{margin:0;padding:0;box-sizing:border-box}
html,body{width:1200px;height:3252px;overflow:hidden;background:var(--white)}
body{position:relative;font-family:"Fira Sans",Arial,sans-serif;font-weight:300;color:var(--text)}
a{text-decoration:none;color:inherit}
.abs{position:absolute}

/* header */
.site-header{position:absolute;left:0;top:0;width:1200px;height:62px;background:var(--white);z-index:5}
.brand{position:absolute;left:92px;top:12px;display:flex;align-items:center;gap:8px;font-weight:600;font-size:26px;color:var(--blue);letter-spacing:.5px}
.brand-dot{width:14px;height:14px;background:var(--red)}
.main-nav{position:absolute;top:20px;left:0;font-size:16px;font-weight:400;color:var(--blue)}
.main-nav a{position:absolute;white-space:nowrap}
.main-nav a.active{color:var(--red)}

/* hero */
.hero{position:absolute;left:0;top:62px;width:1200px;height:630px}
.hero-photo{position:absolute;inset:0;background:linear-gradient(180deg,#28357f 0%,#2e3b8a 45%,#27337b 100%)}
.hero-title{position:absolute;left:0;width:1153px;top:232px;text-align:center;color:var(--white);font-family:"Fira Sans Condensed","Fira Sans",sans-serif;font-weight:400;font-size:47px;line-height:56px}
.hero-dots{position:absolute;top:522px;left:590px;display:flex;gap:8px}
.hero-dots span{width:10px;height:10px;border-radius:50%;background:var(--white)}
.hero-edge{position:absolute;left:0;top:592px;width:1200px;height:100px}

.section-title{position:absolute;left:0;width:1200px;text-align:center;color:var(--blue);font-weight:400;font-size:32px}

/* services */
.service{position:absolute;width:300px;text-align:center}
.service-icon{display:block;margin:0 auto}
.service h3{margin-top:30px;font-weight:400;font-size:19px;color:var(--blue)}
.service p{margin:30px auto 0;width:265px;font-size:14.5px;line-height:19px}
.service a{display:block;margin-top:26px;font-size:13.5px;font-weight:400;color:var(--red)}

/* about band */
.about-band{position:absolute;left:0;top:1250px;width:1200px;height:550px}
.about-photo{position:absolute;left:92px;top:1372px;width:463px;height:352px;background:linear-gradient(120deg,#4e5563 0%,#8a6a4e 45%,#6e5644 70%,#e7e6e4 100%);clip-path:polygon(6% 8%,40% 2%,72% 6%,96% 14%,100% 55%,92% 88%,58% 94%,22% 100%,8% 86%,0 70%,0 26%)}
.about-copy{position:absolute;left:590px;top:1340px;width:510px}
.about-copy h2{font-weight:400;font-size:31px;line-height:38px;color:var(--blue)}
.about-copy p{margin-top:19px;font-size:14.5px;line-height:19px;text-align:justify}
.about-copy h2+p{margin-top:30px}

/* work */
.work-item{position:absolute;width:300px;text-align:center}
.work-photo{width:274px;height:274px;border-radius:50%;margin:0 auto}
.work-item p{margin-top:32px;font-size:15px;line-height:19px}
.arrow{position:absolute;top:2093px}

/* testimonials */
.testimonials{position:absolute;left:0;top:2420px;width:1200px;height:500px}
.testimonial-bg{position:absolute;inset:0;background:linear-gradient(90deg,#5b5451 0%,#625b57 60%,#7a736e 100%)}
.testimonial-title{position:absolute;left:0;width:1155px;top:68px;text-align:center;color:var(--white);font-weight:400;font-size:31px}
.testimonial{position:absolute;top:150px;width:290px;text-align:center;color:var(--white)}
.avatar{width:106px;height:106px;border-radius:50%;margin:0 auto;background:linear-gradient(160deg,#c9b3a3,#8c7466)}
.testimonial h4{margin-top:12px;font-weight:500;font-size:14.5px;line-height:18px}
.testimonial p{margin-top:20px;font-size:14px;line-height:17.5px;font-weight:400}

/* footer */
.footer-cta{position:absolute;left:92px;top:2990px}
.footer-cta h3{font-weight:600;font-size:18.5px;color:var(--blue)}
.footer-cta p{font-size:18.5px;font-weight:400;color:var(--blue);margin-top:1px}
.btn{display:inline-block;margin-top:14px;background:var(--red);color:var(--white);font-size:14.5px;font-weight:400;padding:10px 10px;width:288px;text-align:center}
.footer-heading{position:absolute;top:2982px;font-weight:600;font-size:18px;color:var(--blue)}
.link-list{position:absolute;top:3026px;list-style:none;font-size:13.5px;line-height:27.5px}
.social{position:absolute;left:941px;top:3024px;display:grid;grid-template-columns:repeat(3,22px);column-gap:21px;row-gap:28px}
.social span{width:20px;height:20px;border-radius:50%;border:2px solid #b3b3b3}
.footer-rule{position:absolute;left:92px;top:3205px;width:1016px;height:1px;background:var(--rule)}
.legal{position:absolute;top:3222px;font-size:11.5px;color:#777}
</style>
</head>
<body>

<header class="site-header">
  <a class="brand" href="#"><span class="brand-dot"></span>Halden Painting</a>
  <nav class="main-nav">
    <a class="active" href="#" style="left:499px">Home</a>
    <a href="#" style="left:585px">About Us</a>
    <a href="#" style="left:683px">Residential</a>
    <a href="#" style="left:798px">Multi Family</a>
    <a href="#" style="left:921px">Commercial</a>
    <a href="#" style="left:1034px">Contact Us</a>
  </nav>
</header>

<section class="hero">
  <div class="hero-photo" role="img" aria-label="Painted gym interior with a large blue lettered feature wall, tinted blue"></div>
  <h1 class="hero-title">COMMERCIAL AND RESIDENTIAL<br>PAINT CONTRACTOR</h1>
  <div class="hero-dots"><span></span><span></span><span></span></div>
  <svg class="hero-edge" viewBox="0 0 1200 100" preserveAspectRatio="none">
    <path d="M0 20 L40 18 L90 30 L150 26 L210 38 L300 44 L380 52 L470 58 L540 62 L620 64 L700 70 L780 72 L860 76 L940 78 L1020 80 L1100 80 L1160 78 L1200 76 L1200 100 L0 100 Z" fill="#fff"/>
  </svg>
</section>

<h2 class="section-title" style="top:745px">Thinking About Painting?</h2>

<div class="service" style="left:100px;top:850px">
  <svg class="service-icon" width="156" height="156" viewBox="0 0 156 156">
    <circle cx="78" cy="78" r="70" fill="none" stroke="var(--red)" stroke-width="9"/>
    <g fill="none" stroke="var(--blue)" stroke-width="2.5">
      <rect x="48" y="52" width="60" height="52" rx="3"/><line x1="48" y1="64" x2="108" y2="64"/>
      <line x1="62" y1="46" x2="62" y2="56"/><line x1="94" y1="46" x2="94" y2="56"/>
      <line x1="56" y1="74" x2="100" y2="74" stroke-dasharray="7 4"/><line x1="56" y1="84" x2="100" y2="84" stroke-dasharray="7 4"/><line x1="56" y1="94" x2="100" y2="94" stroke-dasharray="7 4"/>
    </g>
  </svg>
  <h3>Schedule Free Estimate</h3>
  <p>One of the most trusted painting services company in Chicago, we pride that our Chicago Painters.</p>
  <a href="#">Know More</a>
</div>

<div class="service" style="left:437px;top:850px">
  <svg class="service-icon" width="156" height="156" viewBox="0 0 156 156">
    <circle cx="78" cy="78" r="70" fill="none" stroke="var(--red)" stroke-width="9"/>
    <g fill="none" stroke="var(--blue)" stroke-width="3" stroke-linejoin="round">
      <path d="M44 78 L78 46 L112 78"/><path d="M54 70 V108 H102 V70"/><rect x="70" y="86" width="16" height="22"/>
    </g>
  </svg>
  <h3>Residential Services</h3>
  <p>One of the most trusted painting services company in Chicago, we pride that our Chicago Painters.</p>
  <a href="#">Know More</a>
</div>

<div class="service" style="left:764px;top:850px">
  <svg class="service-icon" width="156" height="156" viewBox="0 0 156 156">
    <circle cx="78" cy="78" r="70" fill="none" stroke="var(--red)" stroke-width="9"/>
    <g fill="none" stroke="var(--blue)" stroke-width="2.5">
      <rect x="50" y="46" width="56" height="64"/>
      <rect x="56" y="54" width="8" height="8"/><rect x="68" y="54" width="8" height="8"/><rect x="80" y="54" width="8" height="8"/><rect x="92" y="54" width="8" height="8"/>
      <rect x="56" y="68" width="8" height="8"/><rect x="68" y="68" width="8" height="8"/><rect x="80" y="68" width="8" height="8"/><rect x="92" y="68" width="8" height="8"/>
      <rect x="56" y="82" width="8" height="8"/><rect x="68" y="82" width="8" height="8"/><rect x="80" y="82" width="8" height="8"/><rect x="92" y="82" width="8" height="8"/>
      <rect x="72" y="96" width="12" height="14"/>
    </g>
  </svg>
  <h3>Commercial Services</h3>
  <p>One of the most trusted painting services company in Chicago, we pride that our Chicago Painters.</p>
  <a href="#">Know More</a>
</div>

<svg class="about-band" viewBox="0 0 1200 550" preserveAspectRatio="none">
  <path d="M0 10 L60 6 L120 8 L200 0 L300 4 L420 8 L560 12 L700 16 L840 20 L980 24 L1100 28 L1200 30 L1200 540 L1120 536 L1000 538 L880 536 L760 532 L640 530 L520 526 L400 524 L280 520 L160 514 L60 512 L0 508 Z" fill="var(--band)"/>
</svg>
<div class="about-photo" role="img" aria-label="Reclaimed wood accent wall with painted gym lettering in a grey interior"></div>
<div class="about-copy">
  <h2>Looking for the Best Licensed<br>&amp; Insured Chicago Painters?</h2>
  <p>One of the most trusted painting services company in Chicago, we pride that our Chicago Painters take attention to quality and affordability of your painting services. We offer a wide range of painting services in Chicago and Chicago suburbs.</p>
  <p>Our painting services include painting new and old buildings from private houses and townhouses to apartment buildings and also painting commercial buildings and offices. Halden Chicago painting services guarantees quality painting job, competitive prices and 100% customer satisfaction.</p>
  <p>Halden Chicago Painters Services has skilled and professional painters that are ready to take on any painting project no matter what size. Our painters work hours are adjusted to suit your project and your work schedule.</p>
  <p>Fully licensed &amp; insured for your security and guarantee.</p>
</div>

<h2 class="section-title" style="top:1872px;width:1165px">Our Work</h2>

<svg class="arrow" style="left:80px" width="14" height="24" viewBox="0 0 14 24"><path d="M12 2 L3 12 L12 22" fill="none" stroke="#9a9a9a" stroke-width="2"/></svg>
<svg class="arrow" style="left:1107px" width="14" height="24" viewBox="0 0 14 24"><path d="M2 2 L11 12 L2 22" fill="none" stroke="#9a9a9a" stroke-width="2"/></svg>

<div class="work-item" style="left:94px;top:1966px">
  <div class="work-photo" role="img" aria-label="Freshly painted white kitchen with pendant lights" style="background:radial-gradient(circle at 50% 40%,#eeeeec,#b9b4ae 80%,#6b5a4c)"></div>
  <p>One of the most trusted painting services company in Chicago, we pride that our Chicago Painters.</p>
</div>
<div class="work-item" style="left:449px;top:1966px">
  <div class="work-photo" role="img" aria-label="Bright painted lobby with tall windows and dark seating" style="background:radial-gradient(circle at 45% 35%,#f0f0ee,#b9b8b5 70%,#5f5f5e)"></div>
  <p>One of the most trusted painting services company in Chicago, we pride that our Chicago Painters.</p>
</div>
<div class="work-item" style="left:800px;top:1966px">
  <div class="work-photo" role="img" aria-label="Gym interior with a large blue lettered feature wall" style="background:radial-gradient(circle at 50% 45%,#5a6694,#2b3560 65%,#3b3b3f)"></div>
  <p>One of the most trusted painting services company in Chicago, we pride that our Chicago Painters.</p>
</div>

<section class="testimonials">
  <div class="testimonial-bg" role="img" aria-label="Grey painted wall with colour swatches, a green ladder and paint cans"></div>
  <svg class="abs" style="left:0;top:0" width="1200" height="500" viewBox="0 0 1200 500" preserveAspectRatio="none">
    <path d="M0 0 L1200 0 L1200 2 L1120 6 L1000 12 L880 22 L760 30 L640 40 L520 50 L400 60 L280 66 L160 72 L60 74 L0 76 Z" fill="#fff"/>
    <path d="M0 472 L100 476 L220 468 L360 478 L500 470 L640 480 L780 472 L920 478 L1060 470 L1200 466 L1200 500 L0 500 Z" fill="#fff"/>
  </svg>
  <h2 class="testimonial-title">Client Testimonials</h2>
  <div class="testimonial" style="left:126px">
    <div class="avatar" role="img" aria-label="Client portrait"></div>
    <h4>MARLENE, 37<br>Jahre, Großkorbetha</h4>
    <p>Quisque at magna eu augue semper euismod. Fusce commodo molestie luctus. Donec mollis nulla ipsum, vitae faucibus dui dapibus at. Cras ullamcorper eget ipsum vel volutpat. Phasellus rhoncus in sapien tincidunt mollis.</p>
  </div>
  <div class="testimonial" style="left:456px">
    <div class="avatar" role="img" aria-label="Client portrait"></div>
    <h4>TORVIK, 32<br>Jahre, Großkorbetha</h4>
    <p>Quisque at magna eu augue semper euismod. Fusce commodo molestie luctus. Donec mollis nulla ipsum, vitae faucibus dui dapibus at. Cras ullamcorper eget ipsum vel volutpat. Phasellus rhoncus in sapien tincidunt mollis.</p>
  </div>
  <div class="testimonial" style="left:784px">
    <div class="avatar" role="img" aria-label="Client portrait"></div>
    <h4>NADIA, 32<br>Jahre, Großkorbetha</h4>
    <p>Quisque at magna eu augue semper euismod. Fusce commodo molestie luctus. Donec mollis nulla ipsum, vitae faucibus dui dapibus at. Cras ullamcorper eget ipsum vel volutpat. Phasellus rhoncus in sapien tincidunt mollis.</p>
  </div>
</section>

<footer>
  <div class="footer-cta">
    <h3>Schedule an estimate for FREE today!</h3>
    <p>Call Brightcoat Painting at (555) 014-2290</p>
    <a class="btn" href="#">SCHEDULE YOUR FREE ESTIMATE TODAY!</a>
  </div>

  <h4 class="footer-heading" style="left:495px">Quick Links</h4>
  <ul class="link-list" style="left:495px">
    <li>Residential</li><li>Careers</li><li>California Privacy Policy</li><li>Do Not Sell My Info</li><li>Collection Notice</li>
  </ul>
  <ul class="link-list" style="left:743px">
    <li>Our Locations</li><li>Schedule Estimate</li><li>Warranty</li><li>Site Map</li>
  </ul>

  <h4 class="footer-heading" style="left:943px">Follow Us</h4>
  <div class="social" aria-label="Social profiles">
    <span></span><span></span><span></span><span></span><span></span><span></span>
  </div>

  <div class="footer-rule"></div>
  <p class="legal" style="left:92px">© 2020 Halden Painting All rights reserved.</p>
  <p class="legal" style="left:808px">Privacy Policy</p>
  <p class="legal" style="left:925px">Terms of Use</p>
  <p class="legal" style="left:1038px">Accessibility</p>
</footer>

</body>
</html>
```